Generative AI radar Infographics

I want to create an infographic called "Machine Learning Prospect Compass for Tender Replies". (see slide 3 of the PowerPoint file). I want to use it on social media (ConnectHub and Website). I added 2 inspiration graphics in my brief (see slide 2 of the PowerPoint). I want to add my logo on the infographic. (I also uploaded my company logos). You can find model detailed instructions on slide 1 of the PowerPoint.
Business development and sales
I am a business consultant. I will be using this infographics on Connecthub and in my powerpoint presentations to clients

```html
<!DOCTYPE html>
<html lang="en">
<head>
<meta charset="utf-8">
<title>Machine Learning Prospect Compass for Tender Replies</title>
<link rel="stylesheet" href="https://fonts.googleapis.com/css2?family=Poppins:wght@400;500;600;800&display=swap">
<style>
  :root {
    --page-navy: #0a2d40;
    --ink-navy: #0b2d40;
    --panel: #f1f1f3;
    --teal: #0e94b8;
    --orange: #ef5a2a;
    --grey: #6f6f71;
    --item-ink: #283a47;
  }
  * { box-sizing: border-box; margin: 0; padding: 0; }
  html, body { width: 1200px; height: 1200px; overflow: hidden; }
  body {
    background: var(--page-navy);
    font-family: "Poppins", sans-serif;
    position: relative;
  }
  .panel {
    position: absolute;
    left: 62px; top: 259px;
    width: 1083px; height: 688px;
    background: var(--panel);
  }
  .headline {
    position: absolute;
    left: 0; top: 289px; width: 1200px;
    text-align: center;
    font-weight: 800;
    font-size: 29.4px;
    letter-spacing: -0.4px;
    color: var(--ink-navy);
    white-space: nowrap;
  }
  .headline .accent { color: var(--teal); }
  .radar {
    position: absolute; left: 0; top: 0;
    width: 1200px; height: 1200px;
  }
  .ring-label {
    font-family: "Poppins", sans-serif;
    font-weight: 800;
    font-size: 17px;
    fill: #ffffff;
    letter-spacing: 0.5px;
  }
  .axis-label {
    position: absolute;
    font-weight: 500;
    font-size: 16px;
    line-height: 23px;
    color: var(--ink-navy);
    white-space: nowrap;
  }
  .axis-top { left: 0; width: 1198px; top: 349px; text-align: center; }
  .axis-bottom { left: 0; width: 1198px; top: 896px; text-align: center; }
  .axis-left { right: 871px; top: 597px; text-align: right; }
  .axis-right { left: 861px; top: 607px; }
  .item {
    position: absolute;
    font-size: 9.3px;
    line-height: 14px;
    color: var(--item-ink);
    white-space: nowrap;
    padding-left: 13px;
  }
  .item::before {
    content: "";
    position: absolute;
    left: 0; top: 3.5px;
    width: 7px; height: 7px;
    border-radius: 50%;
    background: var(--dot);
  }
  .decision { --dot: var(--teal); }
  .development { --dot: var(--ink-navy); }
  .capture { --dot: var(--orange); }
  .strategy { --dot: var(--grey); }
  .brand {
    position: absolute;
    left: 832px; top: 860px;
    width: 258px;
    text-align: center;
    color: var(--ink-navy);
    font-weight: 600;
    font-size: 26px;
    line-height: 32px;
    white-space: nowrap;
  }
</style>
</head>
<body>
  <div class="panel"></div>

  <h1 class="headline">MACHINE LEARNING PROSPECT COMPASS FOR <span class="accent">TENDER REPLIES</span></h1>

  <svg class="radar" viewBox="0 0 1200 1200" aria-hidden="true">
    <defs>
      <path id="arc-top-left" d="M374,636 A225,225 0 0 1 599,411"/>
      <path id="arc-top-right" d="M599,411 A225,225 0 0 1 824,636"/>
      <path id="arc-bottom-left" d="M362,636 A237,237 0 0 0 599,873"/>
      <path id="arc-bottom-right" d="M599,873 A237,237 0 0 0 836,636"/>
    </defs>
    <g fill="none" stroke-width="46">
      <path d="M368,636 A231,231 0 0 1 599,405" stroke="var(--teal)"/>
      <path d="M599,405 A231,231 0 0 1 830,636" stroke="var(--ink-navy)"/>
      <path d="M830,636 A231,231 0 0 1 599,867" stroke="var(--grey)"/>
      <path d="M599,867 A231,231 0 0 1 368,636" stroke="var(--orange)"/>
    </g>
    <g stroke="var(--ink-navy)" stroke-width="1">
      <line x1="599" y1="432" x2="599" y2="838"/>
      <line x1="396" y1="636" x2="802" y2="636"/>
    </g>
    <g fill="var(--ink-navy)">
      <polygon points="599,426 594,433 604,433"/>
      <polygon points="599,844 594,837 604,837"/>
      <polygon points="390,636 397,631 397,641"/>
      <polygon points="808,636 801,631 801,641"/>
    </g>
    <text class="ring-label"><textPath href="#arc-top-left" startOffset="52%" text-anchor="middle">DECISION SUPPORT</textPath></text>
    <text class="ring-label"><textPath href="#arc-top-right" startOffset="52%" text-anchor="middle">PROPOSAL DEVELOPMENT</textPath></text>
    <text class="ring-label"><textPath href="#arc-bottom-left" startOffset="52%" text-anchor="middle">CAPTURE STRATEGY</textPath></text>
    <text class="ring-label"><textPath href="#arc-bottom-right" startOffset="50%" text-anchor="middle">PROPOSAL STRATEGY</textPath></text>
  </svg>

  <div class="axis-label axis-top">PROCESS ENHANCEMENT</div>
  <div class="axis-label axis-bottom">STRATEGY ENABLEMENT</div>
  <div class="axis-label axis-left">INSIGHTS GENERATION<br>(TRANSFORMATIVE<br>APPLICATION)</div>
  <div class="axis-label axis-right">TASK AUTOMATION<br>(FOUNDATIONAL USE)</div>

  <div class="item decision" style="left:486px;top:475px">Bid/No Bid Analysis</div>
  <div class="item decision" style="left:469px;top:500px">Bid Qualification</div>
  <div class="item decision" style="left:447px;top:525px">Opportunity assessment</div>
  <div class="item decision" style="left:451px;top:550px">Win Probability modeling</div>
  <div class="item decision" style="left:422px;top:576px">Strategic Pricing optimization</div>
  <div class="item decision" style="left:447px;top:601px">Compliance assessment</div>

  <div class="item development" style="left:605px;top:461px">Company profile</div>
  <div class="item development" style="left:630px;top:479px">CV and Resumes</div>
  <div class="item development" style="left:609px;top:498px">Past Performance</div>
  <div class="item development" style="left:641px;top:516px">Technical solution</div>
  <div class="item development" style="left:621px;top:534px">Compliance Matrix</div>
  <div class="item development" style="left:661px;top:553px">Statement of Work</div>
  <div class="item development" style="left:611px;top:571px">Executive Summary</div>
  <div class="item development" style="left:657px;top:589px">Security Questionnaires</div>
  <div class="item development" style="left:605px;top:608px">Due Diligence Questionnaires</div>

  <div class="item capture" style="left:420px;top:651px">Capture Plan</div>
  <div class="item capture" style="left:468px;top:675px">SWOT Analysis</div>
  <div class="item capture" style="left:425px;top:700px">Customer Hot Buttons</div>
  <div class="item capture" style="left:468px;top:724px">Customer Intelligence</div>
  <div class="item capture" style="left:450px;top:748px">Competitive Intelligence</div>
  <div class="item capture" style="left:488px;top:772px">Value Proposition</div>

  <div class="item strategy" style="left:615px;top:650px">Proposal plan</div>
  <div class="item strategy" style="left:647px;top:679px">Proposal outline</div>
  <div class="item strategy" style="left:618px;top:709px">Key messages extraction</div>
  <div class="item strategy" style="left:634px;top:739px">Win Theme extraction</div>
  <div class="item strategy" style="left:611px;top:768px">Differentiators</div>

  <div class="brand">Ostrand Partners</div>
</body>
</html>
```